GridMonarch : This is a Puzzle and This is not a Puzzle

GridMonarch is a new addictive way to play Sudoku (see description on the attached document).
We would like your help in developing a design for the playscreen of the game (a mock-up is in the attached document)
The winner will be entrusted with the work of the complete design of the application (home screen, configuration screen, etc.) in a specific contract.
Thank you from Paris France.
Best.
Bertrand

```html
<!DOCTYPE html>
<html lang="en">
<head>
<meta charset="utf-8">
<title>GridMonarch – Play Screen</title>
<link href="https://fonts.googleapis.com/css2?family=Inter:wght@400;500;600&display=swap" rel="stylesheet">
<style>
:root{
  --page:#1c4660;
  --screen:#2f2e70;
  --board-zone:#2a2966;
  --board:#29285f;
  --empty:#3b3a82;
  --btn:#43439a;
  --btn-dark:#3b3b88;
  --badge:#1f1e4f;
  --c-blue:#5454ee;
  --c-cyan:#00ffff;
  --c-gold:#cc9200;
  --c-red:#ff5a5a;
  --c-gray:#bfbfbf;
  --c-black:#000000;
  --c-pink:#ff6cf5;
  --c-green:#55e855;
  --c-yellow:#fbf68c;
  --accent:#ff7a1a;
  --text:#ffffff;
}
*{margin:0;padding:0;box-sizing:border-box}
html,body{width:1200px;height:801px;overflow:hidden;background:var(--page);font-family:"Inter",sans-serif;color:var(--text)}
.screen{position:absolute;left:0;top:123px;width:1200px;height:555px;background:var(--screen);border-radius:56px;overflow:hidden}
.board-zone{position:absolute;left:250px;top:0;width:740px;height:555px;background:var(--board-zone)}
.home{position:absolute;left:77px;top:22px;width:60px;height:60px;border-radius:12px;background:#44468f;display:flex;align-items:center;justify-content:center;box-shadow:0 8px 14px rgba(0,0,0,.25)}
.btn{position:absolute;height:53px;border-radius:27px;background:var(--btn);display:flex;align-items:center;gap:10px;padding-left:16px;font-size:14.5px;font-weight:500}
.btn svg{flex:none}
.swatches,.digits{position:absolute;top:39px}
.swatch,.digit{position:absolute;width:38px;height:38px;border-radius:8px;display:flex;align-items:center;justify-content:center;font-size:15px;font-weight:500}
.swatches{left:285px}
.digits{left:920px}
.digit{background:var(--btn);color:#fff;font-size:17px}
.digit .count{position:absolute;right:-7px;bottom:-7px;width:15px;height:15px;border-radius:4px;background:var(--badge);font-size:7.5px;display:flex;align-items:center;justify-content:center}
.board{position:absolute;left:362px;top:20px;width:520px;height:520px;padding:2px;background:var(--board);border-radius:6px;display:grid;grid-template-columns:repeat(3,168px);gap:6px}
.box{display:grid;grid-template-columns:repeat(3,54px);grid-auto-rows:54px;gap:3px}
.cell{border-radius:7px;background:var(--empty);display:flex;align-items:center;justify-content:center;font-size:25px;color:rgba(30,30,50,.6)}
.blue{background:var(--c-blue);color:#2c2c9a}.cyan{background:var(--c-cyan)}.gold{background:var(--c-gold)}
.red{background:var(--c-red)}.gray{background:var(--c-gray)}.black{background:var(--c-black);color:#fff}
.pink{background:var(--c-pink)}.green{background:var(--c-green)}.yellow{background:var(--c-yellow)}
.ghost{color:rgba(20,20,45,.55)}
.tag{position:absolute;height:24px;border-radius:12px;background:var(--btn-dark);font-size:8.5px;font-weight:600;display:flex;align-items:center;padding-left:16px}
.row-icons{position:absolute;display:flex;gap:2px}
</style>
</head>
<body>
<main class="screen">
  <div class="board-zone"></div>

  <div class="home" aria-label="Home">
    <svg width="22" height="22" viewBox="0 0 22 22"><path d="M3 10 11 3l8 7v9H3z" fill="#4ef0f0"/><rect x="9" y="13" width="4" height="6" fill="#44468f"/></svg>
  </div>

  <div class="btn" style="left:75px;top:249px;width:117px">
    <svg width="30" height="26" viewBox="0 0 30 26" fill="none" stroke="#fff" stroke-width="2" stroke-linecap="round"><path d="M9 3 3 9l6 6"/><path d="M3 9h14a8 8 0 0 1 0 16h-5"/></svg>Undo
  </div>
  <div class="btn" style="left:74px;top:326px;width:162px">
    <svg width="26" height="26" viewBox="0 0 26 26"><rect x="1" y="1" width="12" height="12" fill="#ff3b3b"/><rect x="13" y="1" width="12" height="12" fill="#ffd400"/><rect x="1" y="13" width="12" height="12" fill="#2d7bff"/><rect x="13" y="13" width="12" height="12" fill="#30d158"/><ellipse cx="13" cy="13" rx="9" ry="6" fill="#fff"/><circle cx="13" cy="13" r="3" fill="#1f1e4f"/></svg>Number Grids
  </div>
  <div class="btn" style="left:75px;top:403px;width:169px">
    <svg width="28" height="26" viewBox="0 0 28 26"><path d="M12 2 24 14 15 23 3 11z" fill="#fff"/><path d="M8 16l7 7H4l-3-3z" fill="#ff2030"/><path d="M3 24h22" stroke="#fff" stroke-width="2"/></svg>Number Eraser
  </div>
  <div class="btn" style="left:75px;top:469px;width:148px">
    <svg width="22" height="28" viewBox="0 0 22 28"><circle cx="11" cy="10" r="8" fill="#ffd23a"/><path d="M7 16h8v5H7z" fill="#ffd23a"/><rect x="7" y="22" width="8" height="4" rx="2" fill="#b9b9d9"/></svg>Colors Help
  </div>

  <div class="swatches">
    <div class="swatch" style="top:0;background:#ffff4d;color:#a3a300;box-shadow:0 0 14px #ffff4d88">4</div>
    <div class="swatch" style="top:57px;background:#ff00ff;color:#a000a0;box-shadow:0 0 14px #ff00ff88">6</div>
    <div class="swatch" style="top:114px;background:#cc9600;color:#7a5a00;box-shadow:0 0 14px #cc960088">6</div>
    <div class="swatch" style="top:171px;background:#ff0000;color:#a00000;box-shadow:0 0 14px #ff000088">4</div>
    <div class="swatch" style="top:228px;background:#ff9a00;color:#a05f00;box-shadow:0 0 14px #ff9a0088">8</div>
    <div class="swatch" style="top:285px;background:#0000cc;color:#00008a;box-shadow:0 0 14px #0000cc88">4</div>
    <div class="swatch" style="top:342px;background:#22ee22;color:#109010;box-shadow:0 0 14px #22ee2288">5</div>
    <div class="swatch" style="top:399px;background:#33ffff;color:#10a0a0;box-shadow:0 0 14px #33ffff88">7</div>
    <div class="swatch" style="top:456px;background:#000;color:#fff;box-shadow:0 0 14px #00000088">3</div>
  </div>

  <div class="board">
    <div class="box">
      <div class="cell blue">9</div><div class="cell cyan">1</div><div class="cell gold">5</div>
      <div class="cell gray">7</div><div class="cell black">4</div><div class="cell pink">6</div>
      <div class="cell red">8</div><div class="cell green">2</div><div class="cell yellow">3</div>
    </div>
    <div class="box">
      <div class="cell red">7</div><div class="cell gray">2</div><div class="cell black">3</div>
      <div class="cell cyan">8</div><div class="cell green">1</div><div class="cell yellow">5</div>
      <div class="cell pink">9</div><div class="cell gold">6</div><div class="cell blue">4</div>
    </div>
    <div class="box">
      <div class="cell red">7</div><div class="cell gray">2</div><div class="cell black">3</div>
      <div class="cell cyan">8</div><div class="cell green">1</div><div class="cell yellow">5</div>
      <div class="cell pink">9</div><div class="cell gold">6</div><div class="cell blue">4</div>
    </div>
    <div class="box">
      <div class="cell"></div><div class="cell"></div><div class="cell"></div>
      <div class="cell"></div><div class="cell"></div><div class="cell"></div>
      <div class="cell"></div><div class="cell"></div><div class="cell"></div>
    </div>
    <div class="box">
      <div class="cell"></div><div class="cell"></div><div class="cell"></div>
      <div class="cell"></div><div class="cell"></div><div class="cell"></div>
      <div class="cell"></div><div class="cell blue">7</div><div class="cell"></div>
    </div>
    <div class="box">
      <div class="cell yellow">7</div><div class="cell green">2</div><div class="cell gray">3</div>
      <div class="cell blue">8</div><div class="cell gold">1</div><div class="cell cyan">5</div>
      <div class="cell ghost">9</div><div class="cell ghost">6</div><div class="cell red">4</div>
    </div>
    <div class="box">
      <div class="cell black">7</div><div class="cell blue">1</div><div class="cell gray">5</div>
      <div class="cell gold">7</div><div class="cell yellow">4</div><div class="cell cyan">6</div>
      <div class="cell green">8</div><div class="cell pink">2</div><div class="cell red">3</div>
    </div>
    <div class="box">
      <div class="cell"></div><div class="cell"></div><div class="cell red">1</div>
      <div class="cell"></div><div class="cell"></div><div class="cell"></div>
      <div class="cell"></div><div class="cell"></div><div class="cell"></div>
    </div>
    <div class="box">
      <div class="cell"></div><div class="cell"></div><div class="cell"></div>
      <div class="cell"></div><div class="cell"></div><div class="cell"></div>
      <div class="cell"></div><div class="cell"></div><div class="cell"></div>
    </div>
  </div>

  <div class="digits">
    <div class="digit" style="top:0">1<span class="count">7</span></div>
    <div class="digit" style="top:57px">2<span class="count">6</span></div>
    <div class="digit" style="top:114px">3<span class="count">4</span></div>
    <div class="digit" style="top:171px">4<span class="count">5</span></div>
    <div class="digit" style="top:228px">5<span class="count">4</span></div>
    <div class="digit" style="top:285px">6<span class="count">3</span></div>
    <div class="digit" style="top:342px">7<span class="count">5</span></div>
    <div class="digit" style="top:399px">8<span class="count">8</span></div>
    <div class="digit" style="top:456px">9<span class="count">6</span></div>
  </div>

  <div class="tag" style="left:1014px;top:19px;width:96px">Game Difficulty</div>
  <div class="row-icons" style="left:1026px;top:49px">
    <svg width="80" height="16" viewBox="0 0 80 16">
      <g fill="#ff9a1a"><path d="M9 0 2 9h5l-2 7 8-10H8z"/><path d="M25 0l-7 9h5l-2 7 8-10h-5z"/><path d="M41 0l-7 9h5l-2 7 8-10h-5z"/><path d="M57 0l-7 9h5l-2 7 8-10h-5z"/></g>
      <path d="M73 0l-7 9h5l-2 7 8-10h-5z" fill="#1f1e4f"/>
    </svg>
  </div>
  <div class="tag" style="left:1014px;top:81px;width:81px">Player Level</div>
  <div class="row-icons" style="left:1026px;top:110px">
    <svg width="78" height="16" viewBox="0 0 78 16">
      <g fill="#ff5a1a"><path d="M7 0c1 4 6 6 6 10a6 6 0 0 1-12 0c0-3 3-4 3-7 2 1 3 3 3 3z"/><path d="M23 0c1 4 6 6 6 10a6 6 0 0 1-12 0c0-3 3-4 3-7 2 1 3 3 3 3z"/><path d="M39 0c1 4 6 6 6 10a6 6 0 0 1-12 0c0-3 3-4 3-7 2 1 3 3 3 3z"/></g>
      <g fill="#1f1e4f"><path d="M55 0c1 4 6 6 6 10a6 6 0 0 1-12 0c0-3 3-4 3-7 2 1 3 3 3 3z"/><path d="M71 0c1 4 6 6 6 10a6 6 0 0 1-12 0c0-3 3-4 3-7 2 1 3 3 3 3z"/></g>
    </svg>
  </div>

  <div class="btn" style="left:1010px;top:172px;width:129px">
    <svg width="34" height="34" viewBox="0 0 34 34" fill="none" stroke="#fff" stroke-width="2"><circle cx="16" cy="19" r="13"/><path d="M13 3h6M16 3v3M27 7l3 3"/><text x="16" y="23" font-size="10" font-family="Inter,sans-serif" fill="#fff" stroke="none" text-anchor="middle" font-weight="600">60</text></svg>Chrono
  </div>
  <div class="btn" style="left:1010px;top:249px;width:113px">
    <svg width="30" height="26" viewBox="0 0 30 26" fill="none" stroke="#fff" stroke-width="2" stroke-linecap="round"><path d="M21 3l6 6-6 6"/><path d="M27 9H13a8 8 0 0 0-8 8v7"/></svg>Redo
  </div>
  <div class="btn" style="left:1009px;top:326px;width:161px">
    <svg width="28" height="26" viewBox="0 0 28 26" fill="none" stroke="#fff" stroke-width="1.6"><rect x="2" y="2" width="24" height="22" rx="2"/><path d="M10 2v22M18 2v22M2 9h24M2 17h24" stroke-opacity=".5"/><ellipse cx="14" cy="13" rx="9" ry="5.5" fill="#43439a"/><circle cx="14" cy="13" r="2.5"/></svg>Number Grids
  </div>
  <div class="btn" style="left:1010px;top:403px;width:169px">
    <svg width="28" height="26" viewBox="0 0 28 26" fill="none" stroke="#fff" stroke-width="1.8"><path d="M14 2 25 13 16 22 5 11z"/><path d="M9 15l6 6"/><path d="M4 24h20"/></svg>Number Eraser
  </div>
  <div class="btn" style="left:1010px;top:469px;width:166px">
    <svg width="22" height="28" viewBox="0 0 22 28"><circle cx="11" cy="10" r="8" fill="#ffd23a"/><path d="M7 16h8v5H7z" fill="#ffd23a"/><rect x="7" y="22" width="8" height="4" rx="2" fill="#b9b9d9"/></svg>Numbers Help
  </div>
</main>
</body>
</html>
```